Business Card design for a company called Tallow Flame NI

I need a business card design for my oil fired boiler servicing company. I have a logo design already and Im just looking that incorporated into the business card design. card details; Tallow Flame NI
Oil Burner Servicing - Mid Ulster Area
Service Engineer - Owen Marsh
Mobile 07751364927
email - Tallow.Flame.NI@hearthmail.example
www.tallowflameni.example
I carry out Servicing, Commissioning, Fault Finding, Warranty Validation
Target Market(s)
home owners with oil fired central heating
Industry/Entity Type
Business
Contact Information for Business Card
Tallow Flame NI
Tell. 07751364927
Web: www.tallowflameni.example
email Tallow.Flame.NI@Hearthmail.Example
Servicing Fault Finding Commissioning Warranty Validation
Look and feel

```html
<!DOCTYPE html>
<html lang="en">
<head>
<meta charset="utf-8">
<title>Tallow Flame NI – Business Card</title>
<link href="https://fonts.googleapis.com/css2?family=Nunito:wght@700&family=Roboto:ital,wght@0,400;0,500;0,700;1,400&display=swap" rel="stylesheet">
<style>
  :root {
    --board: #cdcdcd;
    --card: #f7f7f7;
    --green: #3db22f;
    --green-deep: #0d9a3c;
    --band-top: #45bd35;
    --band-bottom: #17a332;
    --ink: #333333;
    --rule: #b9dca9;
    --white: #ffffff;
  }
  * { box-sizing: border-box; margin: 0; padding: 0; }
  html, body { width: 1200px; height: 1004px; overflow: hidden; }
  body {
    background: var(--board);
    position: relative;
    font-family: "Roboto", Arial, sans-serif;
  }
  .card {
    position: absolute;
    left: 315px;
    width: 568px;
    height: 343px;
    background: var(--card);
    box-shadow: 6px 8px 10px rgba(0,0,0,0.22);
    overflow: hidden;
  }
  .card--front { top: 148px; }
  .card--back { top: 513px; }

  .brand {
    position: absolute;
    display: flex;
    align-items: center;
  }
  .card--front .brand { left: 76px; top: 103px; }
  .card--back .brand { left: 86px; top: 44px; }
  .brand__dot {
    width: 94px; height: 94px;
    border-radius: 50%;
    background: var(--green);
    flex: none;
  }
  .card--back .brand__dot { width: 90px; height: 90px; }
  .brand__text { margin-left: 14px; }
  .brand__name {
    font-family: "Nunito", Arial, sans-serif;
    font-weight: 700;
    font-size: 41px;
    line-height: 1;
    color: var(--green);
    white-space: nowrap;
  }
  .card--back .brand__name { font-size: 38px; }
  .brand__tagline {
    margin-top: 8px;
    font-size: 11px;
    font-weight: 500;
    letter-spacing: 1.6px;
    color: var(--green);
    text-transform: uppercase;
    white-space: nowrap;
  }
  .card--back .brand__tagline { font-size: 10.5px; letter-spacing: 1.5px; }

  .person {
    position: absolute;
    left: 0; right: 0; top: 178px;
    text-align: center;
  }
  .person__name {
    font-size: 22px;
    font-weight: 700;
    color: var(--green-deep);
  }
  .person__role {
    margin: 6px auto 0;
    width: 450px;
    display: flex;
    align-items: center;
    gap: 10px;
    font-size: 12px;
    font-style: italic;
    color: var(--ink);
  }
  .person__role::before, .person__role::after {
    content: "";
    flex: 1;
    height: 1px;
    background: var(--rule);
  }

  .contacts {
    position: absolute;
    left: 0; right: 0; top: 246px;
    display: flex;
    justify-content: center;
    gap: 8px;
    font-size: 12.5px;
    color: var(--ink);
    white-space: nowrap;
  }
  .contacts__item { display: flex; align-items: center; gap: 4px; }
  .contacts__icon { width: 12px; height: 12px; fill: var(--green-deep); flex: none; }

  .services {
    position: absolute;
    left: 0; right: 0; bottom: 0;
    height: 41px;
    background: linear-gradient(var(--band-top), var(--band-bottom));
    color: var(--white);
    font-size: 14px;
    display: flex;
    align-items: center;
    justify-content: center;
    gap: 8px;
  }
</style>
</head>
<body>

<section class="card card--front">
  <div class="brand">
    <div class="brand__dot"></div>
    <div class="brand__text">
      <div class="brand__name">Tallow Flame NI</div>
      <div class="brand__tagline">Oil Burner Servicing - Mid Ulster Area</div>
    </div>
  </div>
  <div class="services">
    <span>Servicing</span><span>|</span><span>Commissioning</span><span>|</span><span>Fault Finding</span><span>|</span><span>Warranty Validation</span>
  </div>
</section>

<section class="card card--back">
  <div class="brand">
    <div class="brand__dot"></div>
    <div class="brand__text">
      <div class="brand__name">Tallow Flame NI</div>
      <div class="brand__tagline">Oil Burner Servicing - Mid Ulster Area</div>
    </div>
  </div>

  <div class="person">
    <div class="person__name">Owen Marsh</div>
    <div class="person__role">Service Engineer</div>
  </div>

  <div class="contacts">
    <span class="contacts__item">
      <svg class="contacts__icon" viewBox="0 0 24 24" aria-hidden="true"><path d="M6.6 10.8a15.1 15.1 0 0 0 6.6 6.6l2.2-2.2c.3-.3.7-.4 1-.2 1.1.4 2.3.6 3.6.6.6 0 1 .4 1 1V20c0 .6-.4 1-1 1A17 17 0 0 1 3 4c0-.6.4-1 1-1h3.5c.6 0 1 .4 1 1 0 1.3.2 2.5.6 3.6.1.3 0 .7-.2 1z"/></svg>
      07751364927
    </span>
    <span class="contacts__item">
      <svg class="contacts__icon" viewBox="0 0 24 24" aria-hidden="true"><path d="M2 5h20v14H2zm2 2v.4l8 5.2 8-5.2V7zm0 2.8V17h16V9.8l-8 5.2z"/></svg>
      Tallow.Flame.NI@Hearthmail.Example
    </span>
    <span class="contacts__item">
      <svg class="contacts__icon" viewBox="0 0 24 24" aria-hidden="true"><path d="M12 2a10 10 0 1 0 0 20 10 10 0 0 0 0-20zm6.9 6h-3a15.6 15.6 0 0 0-1.4-3.6A8 8 0 0 1 18.9 8zM12 4c.8 1.2 1.5 2.5 1.9 4h-3.8c.4-1.5 1.1-2.8 1.9-4zM4.3 14a8 8 0 0 1 0-4h3.4a16 16 0 0 0 0 4zm.8 2h3a15.6 15.6 0 0 0 1.4 3.6A8 8 0 0 1 5.1 16zm3-8h-3a8 8 0 0 1 4.4-3.6C8.9 5.5 8.4 6.7 8.1 8zM12 20c-.8-1.2-1.5-2.5-1.9-4h3.8c-.4 1.5-1.1 2.8-1.9 4zm2.3-6H9.7a14.7 14.7 0 0 1 0-4h4.6a14.7 14.7 0 0 1 0 4zm.2 5.6c.6-1.1 1.1-2.3 1.4-3.6h3a8 8 0 0 1-4.4 3.6zm1.8-5.6a16 16 0 0 0 0-4h3.4a8 8 0 0 1 0 4z"/></svg>
      www.tallowflameni.example
    </span>
  </div>

  <div class="services">
    <span>Servicing</span><span>|</span><span>Commissioning</span><span>|</span><span>Fault Finding</span><span>|</span><span>Warranty Validation</span>
  </div>
</section>

</body>
</html>
```